Web site for fans of TV series "The Drifter Pass"

1. Description: This is a new web site for the fans of a Western TV series called "The Drifter Pass". It ran for nine seasons from 1962 to 1971.

It is going to be a fan-generated content. The site will use a proprietary social-sharing software in the back-end. The software could be looked as your personal Chatterbox service running on your own domain. In fact, anyone can use this software for any social-sharing need.

A sample of the software running a social-sharing site:
http://www.valtemo.com

The public-facing software has ten sections or modules as follows:

1. Survey
2. Blog
3. Links
4. Video
5. Music
6. Photo
7. Cartoon
8. Photo Album
9. Quotes
10. Follow/Followers (like squawkr)

2. Delivery. Three designs for three pages. I need delivery in PSD, JPG and AI formats..

3. Pages

3.1. Homepage
Example: http://www.valtemo.com

IMPORTANT REQUIREMENT. The Homepage should be designed such that I or the site Admin with basic knowledge of HTML and CSS can move around different sections or modules without a need to rewrite the CSS or HTML code.

3.2. Point of Entry or Summary page.
Example: http://valtemo.com/vksp/blog/latest/

3.3. Detail page
Example: http://valtemo.com/vksp/blog/2929/

Project Deadline Extended
Reason: I received acceptable designs late. I would like to give this contest 7 more days. This gives me time to work with current designs and just in case I receive new designs.

Target Market(s)

Age: Above 40, average age is 50-55

Gender: Primarily female

Location: Primarily United States, but we have a visible following in Europe and South America.

Industry/Entity Type

Tv

Requirements
Must have
• 1. The image/icon of The Drifter Pass. You can capture it via ClipHollow clips at the opening of the show.

2. Red color (burgundy. See shirt of the main character called Drifter played by actor Walter Penhale.

3. The American West spirit (yes, you may call it the cowboy spirit)

4. The Homepage should be designed such that a person with basic knowledge of CSS and HTML coding can move around different sections or modules.
Should not have
• No cartoonish icons.

```html
<!DOCTYPE html>
<html lang="en">
<head>
<meta charset="utf-8">
<title>The Drifter Pass – Fan Site</title>
<link href="https://fonts.googleapis.com/css2?family=Roboto+Condensed:wght@400;700&family=Arimo:wght@400;700&family=Kaushan+Script&display=swap" rel="stylesheet">
<style>
:root{
  --parchment:#f0cf86;
  --parchment-light:#f4e2b4;
  --parchment-dark:#e7b862;
  --burgundy:#9b2323;
  --burgundy-dark:#7e1717;
  --band-grey:#5f5f5f;
  --band-pale:#9a9a9a;
  --khaki:#a08f52;
  --ink:#2a2118;
  --muted:#6b6256;
  --white:#ffffff;
  --rule:#d6d0c4;
}
*{box-sizing:border-box;margin:0;padding:0}
html,body{width:820px;height:1200px;overflow:hidden}
body{
  position:relative;
  font-family:"Arimo",Arial,sans-serif;
  color:var(--ink);
  background:
    radial-gradient(ellipse at 50% 18%, rgba(232,222,196,.9) 0%, rgba(232,222,196,0) 55%),
    linear-gradient(180deg,#e6d6aa 0%,var(--parchment) 38%,var(--parchment-dark) 100%);
}
.abs{position:absolute}

/* Header */
.brand{left:150px;top:8px;width:110px;text-align:center;font-family:"Roboto Condensed",sans-serif;font-weight:700;color:var(--burgundy);line-height:1;white-space:nowrap}
.brand .small{font-size:10px;display:block}
.brand .big{font-size:15px;display:block;margin-top:3px;letter-spacing:.2px}
.brand-rule{left:160px;top:40px;width:90px;height:1px;background:var(--burgundy)}
.account{left:528px;top:9px;display:flex;gap:4px}
.account a{display:block;height:14px;width:53px;text-align:center;background:var(--khaki);color:var(--white);font:700 7px/14px "Roboto Condensed",sans-serif;text-transform:uppercase;text-decoration:none;letter-spacing:.3px}
.account a.register{width:53px}
.main-nav{left:366px;top:36px;display:flex;font:700 9.4px/12px "Roboto Condensed",sans-serif;text-transform:uppercase;letter-spacing:.2px}
.main-nav a{color:var(--burgundy-dark);text-decoration:none;padding:0 6.5px;border-left:1px solid rgba(126,23,23,.35)}
.main-nav a:first-child{border-left:0;padding-left:0}
.main-nav a:last-child{padding-right:0}

.backdrop-left{left:0;top:120px;width:190px;height:170px;background:radial-gradient(ellipse at 40% 60%,rgba(170,150,110,.45),rgba(170,150,110,0) 70%)}
.backdrop-right{left:610px;top:50px;width:210px;height:240px;background:radial-gradient(ellipse at 50% 55%,rgba(185,140,90,.45),rgba(185,140,90,0) 70%)}

.hero{left:180px;top:66px;width:448px;height:286px;
  background:
    linear-gradient(180deg,rgba(0,0,0,0) 55%,rgba(40,35,28,.55) 78%,rgba(90,84,74,.6) 100%),
    linear-gradient(90deg,#6d675c 0%,#9a9488 30%,#7d776b 55%,#a39d90 80%,#6a645a 100%),
    linear-gradient(180deg,#b9b4a8 0%,#8e887c 40%,#5c564c 100%);
  background-blend-mode:normal,multiply,normal;
  clip-path:polygon(1% 2%,20% 0,45% 1.5%,70% 0,99% 1%,100% 30%,99% 65%,100% 98%,75% 100%,50% 98.5%,22% 100%,0 99%,1% 60%,0 25%)}
.slider-dots{left:397px;top:353px;display:flex;gap:2px}
.slider-dots span{width:5px;height:5px;border-radius:50%;background:#b7ab8c}
.slider-dots span.on{background:#8a7d5a}
.ornament-rule{height:2px;background:var(--burgundy);opacity:.75}

/* Content panel */
.panel{left:170px;top:392px;width:479px;height:601px;background:var(--white);box-shadow:0 1px 4px rgba(0,0,0,.15)}
.col-divider{left:464px;top:436px;width:0;height:536px;border-left:1px dashed var(--rule)}

.banner{position:absolute;display:flex;align-items:center;padding-left:14px;color:var(--white);font-family:"Kaushan Script",cursive;clip-path:polygon(1% 12%,15% 0,40% 8%,60% 0,85% 6%,99% 0,100% 40%,98% 88%,75% 100%,50% 92%,25% 100%,2% 92%,0 55%)}
.banner.red{background:var(--burgundy)}
.banner.grey{background:var(--band-grey)}
.banner.pale{background:var(--band-pale)}
.banner.lg{font-size:14px}
.banner.md{font-size:12px}

.rule-dash{position:absolute;height:0;border-top:1px dashed var(--rule)}

.survey-q{left:193px;top:451px;font-size:8px;font-weight:700}
.survey-q b{font-size:13px;margin-right:3px}
.option{position:absolute;font-size:6.5px;color:var(--muted);display:flex;align-items:center;gap:6px}
.option i{display:block;width:6px;height:6px;border-radius:50%;background:#c9c4bb}
.option i.on{background:#6b5e30}
.opt-split{left:284px;top:474px;height:20px;border-left:1px dashed var(--rule)}
.btn-submit{left:193px;top:506px;width:105px;height:17px;background:var(--khaki);color:var(--white);font:700 7px/17px "Arimo",sans-serif;text-align:center;text-transform:uppercase;border:1px solid #857640}
.view-all{position:absolute;font-family:"Kaushan Script",cursive;color:var(--burgundy);font-size:8.5px}

.blog-item{position:absolute;left:193px;width:250px}
.blog-item h3{font-size:7.4px;color:var(--burgundy);font-weight:700;letter-spacing:-.1px}
.blog-item p{font-size:5.2px;line-height:7px;color:var(--muted);margin-top:3px}
.blog-item .foot{display:flex;justify-content:space-between;margin-top:4px;font-size:5.2px}
.blog-item .foot b{color:var(--ink)}
.meta{color:var(--burgundy);display:flex;gap:4px}
.meta span+span::before{content:"|";color:#aaa;margin-right:4px}

.thumb{position:absolute;top:922px;width:57px;height:55px;border:2px solid #d9d9d9;outline:1px solid #aaa}

/* Right column */
.video{position:absolute;left:485px;width:150px;height:89px;background:
  linear-gradient(90deg,rgba(30,22,16,.5),rgba(30,22,16,0) 30%,rgba(30,22,16,0) 70%,rgba(30,22,16,.5)),
  linear-gradient(180deg,#3d2f23 0%,#6c5238 45%,#8a6a45 72%,#3a2c20 100%)}
.video .play{position:absolute;left:59px;top:26px;width:32px;height:32px;border-radius:50%;background:rgba(120,120,120,.75)}
.video .play::after{content:"";position:absolute;left:13px;top:9px;border-left:11px solid #e8e8e8;border-top:7px solid transparent;border-bottom:7px solid transparent}
.video .bar{position:absolute;left:0;bottom:0;width:100%;height:9px;background:#111;display:flex;align-items:center;padding:0 4px;gap:4px;font-size:4px;color:#ccc}
.video .bar .track{flex:1;height:2px;background:#555;position:relative}
.video .bar .track::before{content:"";position:absolute;left:0;top:0;width:45%;height:2px;background:#c41b1b}
.video-meta{position:absolute;left:485px;display:flex;gap:4px;font-size:4.6px;align-items:flex-end}
.avatar-sq{width:14px;height:14px;background:linear-gradient(135deg,#c9bda8,#7d7262);border:1px solid #ccc}
.video-meta .who b{display:block;font-size:4.8px}
.pager{left:489px;top:721px;display:flex;gap:5px}
.pager span{display:block;min-width:9px;height:9px;padding:0 2px;border:1px solid #ccc;font-size:5px;line-height:8px;text-align:center;color:#777}
.pager span.on{background:#6b6b6b;color:#fff;border-color:#6b6b6b}
.pager span.wide{width:16px}
.music{left:480px;top:774px;width:154px;height:76px;background:linear-gradient(180deg,#d9d9d9,#cbcbcb)}
.music .seek{position:absolute;left:10px;top:19px;width:134px;height:3px;background:#9b9b9b;border-radius:2px}
.music .seek::before{content:"";position:absolute;left:44px;top:-2px;width:6px;height:6px;border-radius:50%;background:#eee;border:1px solid #888}
.music .ctrl{position:absolute;top:38px;width:11px;height:11px;border-radius:50%;background:#666}
.music .playbig{position:absolute;left:66px;top:32px;width:22px;height:22px;border-radius:50%;background:var(--burgundy)}
.music .playbig::after{content:"";position:absolute;left:8px;top:6px;border-left:8px solid #fff;border-top:5px solid transparent;border-bottom:5px solid transparent}
.cartoon{left:482px;top:894px;width:150px;height:74px;background:
  radial-gradient(ellipse at 50% 55%,#f6e27c 0%,rgba(246,226,124,0) 60%),
  linear-gradient(90deg,#dfe8f0,#f7ecbc 50%,#dfe8f0)}
.cartoon .playbtn{position:absolute;left:67px;top:31px;width:14px;height:14px;border-radius:50%;background:var(--burgundy)}
.cartoon .playbtn::after{content:"";position:absolute;left:5px;top:4px;border-left:5px solid #fff;border-top:3px solid transparent;border-bottom:3px solid transparent}

/* Quotes */
.quotes-title{left:340px;top:1024px;width:140px;text-align:center;font-family:"Kaushan Script",cursive;color:var(--burgundy);font-size:16px;font-weight:400}
.quote{position:absolute;top:1050px;display:flex;gap:10px;width:220px}
.quote .portrait{flex:none;width:44px;height:44px;border-radius:50%;background:radial-gradient(circle at 50% 45%,#e6ddd0 0%,#a8998a 45%,#4b3f33 100%);border:3px solid #b0a06c}
.quote p{font-size:5.6px;line-height:7.3px;color:#3c3328}
.quote cite{display:block;font-style:normal;color:var(--burgundy);font-size:5.8px;margin-top:3px}
.quotes-split{left:414px;top:1054px;height:36px;border-left:1px solid rgba(0,0,0,.15)}

/* Footer */
.site-footer{left:0;top:1134px;width:820px;height:66px;background:var(--burgundy);clip-path:polygon(0 6%,10% 2%,20% 7%,30% 1%,40% 6%,50% 0,60% 6%,70% 2%,80% 7%,90% 1%,100% 5%,100% 100%,0 100%)}
.contact{left:192px;top:1151px;color:var(--white);font-family:"Roboto Condensed",sans-serif}
.contact .row{display:flex;align-items:center;gap:7px}
.contact .phone{font-size:12px}
.contact .mail{font-size:7px;margin-top:5px}
.contact .sep{width:1px;height:11px;background:rgba(255,255,255,.5)}
.foot-split{position:absolute;top:1150px;height:36px;border-left:1px dashed rgba(255,255,255,.35)}
.social{left:371px;top:1153px;color:var(--white);font:400 9px "Roboto Condensed",sans-serif}
.social .icons{display:flex;gap:3px;margin-top:4px;margin-left:2px}
.social .icons span{width:13px;height:13px;border-radius:50%;background:#f1e6e6}
.copyright{left:530px;top:1160px;color:#f2dada;font-size:5.6px;line-height:7px}
</style>
</head>
<body>

<header>
  <div class="abs brand"><span class="small">THE</span><span class="big">DRIFTER PASS</span></div>
  <div class="abs brand-rule"></div>
  <div class="abs account"><a class="login" href="#">Login</a><a class="register" href="#">Register</a></div>
  <nav class="abs main-nav">
    <a href="#">Home</a><a href="#">About Us</a><a href="#">Content</a><a href="#">Post</a><a href="#">Blog</a><a href="#">Contact Us</a>
  </nav>
</header>

<div class="abs backdrop-left" role="img" aria-label="Faded sepia scene of cowboys at work"></div>
<div class="abs backdrop-right" role="img" aria-label="Faded silhouette of a cowboy on horseback"></div>

<section>
  <div class="abs hero" role="img" aria-label="Vintage sepia photograph of cowboys resting by a fence with chaps hanging on barbed wire"></div>
  <div class="abs slider-dots"><span class="on"></span><span></span><span></span><span></span></div>
  <div class="abs ornament-rule" style="left:366px;top:368px;width:88px"></div>
</section>

<main>
  <div class="abs panel"></div>
  <div class="abs col-divider"></div>

  <div class="banner red lg" style="left:186px;top:410px;width:258px;height:32px">Featured Survey</div>
  <div class="abs survey-q"><b>Q:</b>Which of the following Cowboy rides more Bulls?</div>
  <div class="option" style="left:194px;top:471px"><i></i>Hal Brenner</div>
  <div class="option" style="left:194px;top:485px"><i class="on"></i>Lou Ferris</div>
  <div class="abs opt-split"></div>
  <div class="option" style="left:316px;top:471px"><i></i>Otis Crane</div>
  <div class="option" style="left:316px;top:485px"><i></i>Wade Colter</div>
  <div class="abs btn-submit">Sumit your answer!</div>
  <div class="rule-dash" style="left:193px;top:534px;width:245px"></div>
  <div class="view-all" style="left:360px;top:543px">View All Surveys</div>
  <div class="rule-dash" style="left:193px;top:564px;width:245px"></div>

  <div class="banner pale lg" style="left:190px;top:580px;width:254px;height:32px">Blogs</div>

  <article class="blog-item" style="top:625px">
    <h3>Lorem Ipsum is simply dummy text of the printing &amp; typesetting industry.</h3>
    <p>Lorem Ipsum is simply dummy text of the printing and typesetting industry. Lorem Ipsum has been the industry's standard dummy text ever since the 1500s.</p>
    <div class="foot"><b>Read Full Blog</b><div class="meta"><span>6 Hour Ago</span><span>Like</span><span>Share</span><span>Comment</span></div></div>
  </article>
  <div class="rule-dash" style="left:193px;top:674px;width:245px"></div>
  <article class="blog-item" style="top:682px">
    <h3>Lorem Ipsum is simply dummy text of the printing &amp; typesetting industry.</h3>
    <p>Lorem Ipsum is simply dummy text of the printing and typesetting industry. Lorem Ipsum has been the industry's standard dummy text ever since the 1500s.</p>
    <div class="foot"><b>Read Full Blog</b><div class="meta"><span>6 Hour Ago</span><span>Like</span><span>Share</span><span>Comment</span></div></div>
  </article>
  <div class="rule-dash" style="left:193px;top:730px;width:245px"></div>
  <article class="blog-item" style="top:738px">
    <h3>Lorem Ipsum is simply dummy text of the printing &amp; typesetting industry.</h3>
    <p>Lorem Ipsum is simply dummy text of the printing and typesetting industry. Lorem Ipsum has been the industry's standard dummy text ever since the 1500s.</p>
    <div class="foot"><b>Read Full Blog</b><div class="meta"><span>6 Hour Ago</span><span>Like</span><span>Share</span><span>Comment</span></div></div>
  </article>
  <div class="rule-dash" style="left:193px;top:787px;width:245px"></div>
  <article class="blog-item" style="top:795px">
    <h3>Lorem Ipsum is simply dummy text of the printing &amp; typesetting industry.</h3>
    <p>Lorem Ipsum is simply dummy text of the printing and typesetting industry. Lorem Ipsum has been the industry's standard dummy text ever since the 1500s.</p>
    <div class="foot"><b>Read Full Blog</b><div class="meta"><span>6 Hour Ago</span><span>Like</span><span>Share</span><span>Comment</span></div></div>
  </article>
  <div class="rule-dash" style="left:193px;top:843px;width:245px"></div>
  <div class="view-all" style="left:373px;top:851px">View All Blogs</div>
  <div class="rule-dash" style="left:193px;top:872px;width:245px"></div>

  <div class="banner grey lg" style="left:188px;top:886px;width:256px;height:26px">Photo Album</div>
  <div class="thumb" style="left:194px;background:linear-gradient(180deg,#e4e4e4 0%,#a9a9a9 45%,#555 100%)" role="img" aria-label="Black and white photo of a rider on horseback"></div>
  <div class="thumb" style="left:258px;background:linear-gradient(180deg,#dcc3b6 0%,#a87a6a 50%,#6e4538 100%)" role="img" aria-label="Sepia group portrait of the cast"></div>
  <div class="thumb" style="left:322px;background:linear-gradient(180deg,#e3e6e8 0%,#8b8d8f 45%,#2c2c2c 100%)" role="img" aria-label="Black and white photo of a cowboy under the sky"></div>
  <div class="thumb" style="left:387px;background:radial-gradient(ellipse at 55% 55%,#6d6d6d 0%,#b4b4b4 45%,#e0e0e0 100%)" role="img" aria-label="Photo of a vintage revolver"></div>

  <div class="banner grey md" style="left:480px;top:410px;width:155px;height:26px">Videos</div>
  <div class="video" style="top:446px" role="img" aria-label="Video still of riders on horseback">
    <div class="play"></div>
    <div class="bar"><span>&#9654;</span><div class="track"></div><span>1:26 / 3:22</span><span>HD</span></div>
  </div>
  <div class="video-meta" style="top:540px"><div class="avatar-sq" role="img" aria-label="Member avatar"></div><div class="who"><b>Ned Hollis</b>6 Hour Ago</div><div class="meta" style="color:var(--ink)"><span>Like</span><span>Share</span><span>Comment</span></div></div>
  <div class="rule-dash" style="left:494px;top:572px;width:130px"></div>
  <div class="video" style="top:590px" role="img" aria-label="Video still of riders on horseback">
    <div class="play"></div>
    <div class="bar"><span>&#9654;</span><div class="track"></div><span>1:26 / 3:22</span><span>HD</span></div>
  </div>
  <div class="video-meta" style="top:684px"><div class="avatar-sq" role="img" aria-label="Member avatar"></div><div class="who"><b>Ned Hollis</b>6 Hour Ago</div><div class="meta" style="color:var(--ink)"><span>Like</span><span>Share</span><span>Comment</span></div></div>
  <div class="abs pager"><span class="wide">&laquo;</span><span>1</span><span>2</span><span class="on">3</span><span>4</span><span>7</span><span>8</span><span>9</span><span class="wide">&raquo;</span></div>

  <div class="banner grey md" style="left:480px;top:748px;width:154px;height:26px">Drifter Music</div>
  <div class="abs music">
    <div class="seek"></div>
    <div class="ctrl" style="left:55px"></div>
    <div class="ctrl" style="left:88px"></div>
    <div class="playbig"></div>
  </div>

  <div class="banner red md" style="left:480px;top:874px;width:154px;height:22px">Drifter Cartoons</div>
  <div class="abs cartoon" role="img" aria-label="Cartoon of two cowboys in a standoff"><div class="playbtn"></div></div>
</main>

<section>
  <div class="abs ornament-rule" style="left:374px;top:1019px;width:88px"></div>
  <h2 class="abs quotes-title">Quotes</h2>
  <div class="quote" style="left:190px">
    <div class="portrait" role="img" aria-label="Portrait of the quoted fan"></div>
    <div><p>Nulla volutpat felis massa, eu viverra libero venenatis in. Sed nec tristique erat, ut fringilla velit. Nunc interdum quis magna at dictum.Nulla volutpat felis massa.</p><cite>Clara Dunmore</cite></div>
  </div>
  <div class="abs quotes-split"></div>
  <div class="quote" style="left:435px">
    <div class="portrait" role="img" aria-label="Portrait of the quoted fan"></div>
    <div><p>Nulla volutpat felis massa, eu viverra libero venenatis in. Sed nec tristique erat, ut fringilla velit. Nunc interdum quis magna at dictum.Nulla volutpat felis massa.</p><cite>Clara Dunmore</cite></div>
  </div>
  <div class="abs ornament-rule" style="left:374px;top:1106px;width:88px"></div>
</section>

<footer>
  <div class="abs site-footer"></div>
  <div class="abs contact">
    <div class="row phone">
      <svg width="11" height="11" viewBox="0 0 24 24" aria-hidden="true"><path fill="#fff" d="M6.6 10.8a15 15 0 006.6 6.6l2.2-2.2a1 1 0 011-.25 11.4 11.4 0 003.6.57 1 1 0 011 1V20a1 1 0 01-1 1A17 17 0 013 4a1 1 0 011-1h3.5a1 1 0 011 1c0 1.25.2 2.45.57 3.57a1 1 0 01-.25 1z"/></svg>
      <span class="sep"></span><span>08 4417 2390</span>
    </div>
    <div class="row mail">
      <svg width="12" height="9" viewBox="0 0 24 18" aria-hidden="true"><rect x="1" y="1" width="22" height="16" fill="none" stroke="#fff" stroke-width="2"/><path d="M1 1l11 9 11-9" fill="none" stroke="#fff" stroke-width="2"/></svg>
      <span class="sep"></span><span>info@drifterfans.com</span>
    </div>
  </div>
  <div class="foot-split" style="left:330px"></div>
  <div class="abs social">WE ARE SOCIAL...
    <div class="icons"><span role="img" aria-label="Chatterbox"></span><span role="img" aria-label="squawkr"></span><span role="img" aria-label="Professional network"></span><span role="img" aria-label="RSS feed"></span></div>
  </div>
  <div class="foot-split" style="left:490px"></div>
  <div class="abs copyright">Copyright 2013, the Drifter Pass Fans,<br>All Rights Reserved</div>
</footer>

</body>
</html>
```